Internal Designs and HTML Prototype

A Home page design has been completed. The remaining 6 pages need to be designed based on the provided wireframes and the home page design. HTML conversion to be performed to the following standards; - XHTML 1.0 Transitional - Fixed width - Cross-browser compatibility - Safari 2&3, Opera 9 etc - Relative Font sizes - Table-less forms - JQuery as preferred Javascript library - SEO and loading optimoisation

The selected designer will be required to provide the HTML prototype for their layouts.

Target Market(s)

Ensure style of provided Home page is followed.

Industry/Entity Type

Real Estate

```html
<!DOCTYPE html>
<html lang="en">
<head>
<meta charset="utf-8">
<title>HomeTrade – Property Search</title>
<link rel="stylesheet" href="https://fonts.googleapis.com/css2?family=Arimo:wght@400;700&family=Saira+Semi+Condensed:wght@500;600;700&display=swap">
<style>
:root{
  --page-bg:#dcebc6;
  --orange:#f26a12;
  --orange-dark:#d44d06;
  --red-band:#e8331c;
  --nav-green:#6e856d;
  --nav-green-dark:#5b6f5a;
  --frame-green:#6c806b;
  --heading-grey:#6f7f6c;
  --card-frame:#a59f99;
  --peach:#fde2c4;
  --text:#111;
  --field-border:#f08a3c;
  --select-btn:#e5884a;
}
*{box-sizing:border-box;margin:0;padding:0}
html,body{width:798px;height:1200px;overflow:hidden}
body{background:var(--page-bg);font-family:"Arimo",Arial,sans-serif;color:var(--text);position:relative}

.site-header{position:absolute;left:0;top:0;width:798px;height:138px;
  background:linear-gradient(100deg,#3f6d22 0%,#5a8a30 35%,#4d7a2a 60%,#6b8d3d 80%,#8aa35a 100%)}
.brand{position:absolute;left:30px;top:44px;display:flex;align-items:center;gap:12px}
.brand-mark{width:34px;height:34px;background:var(--orange);border-radius:4px}
.brand-name{font-family:"Saira Semi Condensed",sans-serif;font-weight:700;font-size:40px;color:#fff;line-height:1}

.tagline-band{position:absolute;left:0;top:138px;width:798px;height:37px;
  background:linear-gradient(180deg,#f0522e 0%,var(--red-band) 60%,#c92815 100%);
  border-bottom:2px solid #fff}
.tagline{position:absolute;left:22px;top:7px;color:#fff;font-size:18px;font-family:"Arimo",sans-serif}
.login{position:absolute;right:20px;top:13px;display:flex;align-items:center;gap:4px;
  font-size:7px;font-weight:700;color:#fff;letter-spacing:.2px}
.login input{width:87px;height:11px;border:0;background:#fff;margin-right:3px}
.login .sign-in{width:42px;height:12px;background:#7c8b7a;border:1px solid #fff;color:#fff;
  font-size:7px;font-weight:700;display:flex;align-items:center;justify-content:center}

.side-nav{position:absolute;left:12px;top:192px;width:96px}
.side-nav a{display:flex;align-items:center;justify-content:center;text-align:center;
  height:57px;margin-bottom:4px;background:var(--nav-green);border:2px solid #fff;border-right:0;
  border-radius:6px 0 0 6px;color:#fff;text-decoration:none;font-family:"Saira Semi Condensed",sans-serif;
  font-weight:600;font-size:15px;line-height:18px;box-shadow:0 1px 2px rgba(0,0,0,.25)}
.side-nav a.current{background:#fff;color:var(--orange);position:relative;z-index:2;width:98px}

.content-frame{position:absolute;left:106px;top:190px;width:684px;height:975px;
  background:var(--frame-green);border-radius:10px;padding:6px}
.content-panel{width:100%;height:100%;border-radius:7px;border:2px solid #fff;
  background:linear-gradient(90deg,#fff 0%,#fff 52%,var(--peach) 100%);position:relative}

.page-title{position:absolute;left:27px;top:42px;font-family:"Saira Semi Condensed",sans-serif;
  font-weight:700;font-size:21px;color:var(--orange);letter-spacing:.3px}
.section-title{position:absolute;left:27px;top:80px;font-size:14px;font-weight:700;color:var(--heading-grey);letter-spacing:.3px}

.field{position:absolute;width:193px}
.field label{display:block;font-size:9.5px;letter-spacing:.6px;margin-bottom:3px}
.select,.text-input{height:21px;border:1px solid var(--field-border);background:#fff;position:relative;
  font-size:9px;padding:5px 6px;color:#555}
.select::after{content:"";position:absolute;right:2px;top:2px;width:15px;height:15px;
  background:var(--select-btn);border:1px solid #a9562a;border-radius:2px}
.select svg{position:absolute;right:6px;top:8px;z-index:1}
.links{font-size:12px;color:var(--orange);margin-top:4px}
.links a{color:var(--orange)}
.price-pair{display:flex;gap:8px}
.price-pair .select{width:92px}
.continue{position:absolute;left:462px;top:229px;width:73px;height:22px;border-radius:4px;
  background:linear-gradient(180deg,#ff8a3c,var(--orange-dark));color:#fff;font-size:10px;font-weight:700;
  display:flex;align-items:center;justify-content:center;box-shadow:0 1px 2px rgba(0,0,0,.4)}

.listing-grid{position:absolute;left:27px;top:286px;display:grid;grid-template-columns:repeat(3,192px);
  column-gap:24px;row-gap:20px}
.listing-card{height:315px;border:7px solid var(--card-frame);border-radius:8px;background:#fff;padding:6px 7px;font-size:10.5px;line-height:14px}
.listing-photo{height:114px;background:linear-gradient(180deg,#3c6fc4 0%,#5a8ad8 40%,#4a6b3e 60%,#3f5a2c 100%);margin-bottom:6px}
.listing-card h3{font-size:10.5px;font-weight:700}
.listing-card b{font-weight:700}
.divider{border-top:1px dashed #777;margin:7px 0 5px}
</style>
</head>
<body>
<header class="site-header" role="img" aria-label="Family relaxing on green grass">
  <div class="brand"><span class="brand-mark"></span><span class="brand-name">HomeTrade</span></div>
</header>
<div class="tagline-band">
  <p class="tagline">The place to sell. The place to buy.</p>
  <div class="login">USER NAME <input type="text" aria-label="User name"> PASSWORD <input type="password" aria-label="Password"><span class="sign-in">SIGN IN</span></div>
</div>

<nav class="side-nav">
  <a href="#">Home</a>
  <a href="#" class="current">Property<br>Search</a>
  <a href="#">How<br>It Works</a>
  <a href="#">My<br>Account</a>
  <a href="#">Contact</a>
</nav>

<main class="content-frame">
  <div class="content-panel">
    <h1 class="page-title">PROPERTY SEARCH</h1>
    <h2 class="section-title">Property to sell</h2>

    <div class="field" style="left:27px;top:110px"><label>PROPERTY TYPE</label><div class="select">ANY</div></div>
    <div class="field" style="left:243px;top:110px"><label>BEDROOMS</label><div class="select">ANY</div></div>
    <div class="field" style="left:461px;top:110px"><label>BATHROOMS</label><div class="select">ANY</div></div>
    <div class="field" style="left:27px;top:162px"><label>STATE</label><div class="select">ANY</div></div>
    <div class="field" style="left:243px;top:162px"><label>SUBURB</label><div class="text-input"></div>
      <p class="links"><a href="#">Refresh</a> | <a href="#">Clear</a></p></div>
    <div class="field" style="left:461px;top:162px"><label>CARSPACESS</label><div class="select">ANY</div></div>
    <div class="field" style="left:27px;top:214px"><label>PRICE RANGE</label>
      <div class="price-pair"><div class="select">ANY</div><div class="select">ANY</div></div></div>
    <div class="continue">CONTINUE</div>

    <section class="listing-grid">
      <article class="listing-card"><div class="listing-photo" role="img" aria-label="Photo of a single-storey house with trees"></div>
        <h3>The House I'm Swapping</h3><p><b>Bed:</b> x &nbsp;<b>Bath:</b> x</p><p><b>Type:</b> xxxxxxxxxxx</p><p><b>Asking Price:</b> $xxxxxxxxx</p><p><b>In:</b> xxxxxxx</p>
        <div class="divider"></div><h3>Want T o House Swap With</h3><p><b>Bed:</b> xx &nbsp;<b>Bath:</b> xx</p><p><b>Type:</b> xxxxxxxxxxxxxxx</p><p><b>In:</b> xxxxxxxxxxxxx</p><p><b>Price Range:</b></p><p>$xxxxxxxxxxxxxxxx</p></article>
      <article class="listing-card"><div class="listing-photo" role="img" aria-label="Photo of a single-storey house with trees"></div>
        <h3>The House I'm Swapping</h3><p><b>Bed:</b> x &nbsp;<b>Bath:</b> x</p><p><b>Type:</b> xxxxxxxxxxx</p><p><b>Asking Price:</b> $xxxxxxxxx</p><p><b>In:</b> xxxxxxx</p>
        <div class="divider"></div><h3>Want T o House Swap With</h3><p><b>Bed:</b> xx &nbsp;<b>Bath:</b> xx</p><p><b>Type:</b> xxxxxxxxxxxxxxx</p><p><b>In:</b> xxxxxxxxxxxxx</p><p><b>Price Range:</b></p><p>$xxxxxxxxxxxxxxxx</p></article>
      <article class="listing-card"><div class="listing-photo" role="img" aria-label="Photo of a single-storey house with trees"></div>
        <h3>The House I'm Swapping</h3><p><b>Bed:</b> x &nbsp;<b>Bath:</b> x</p><p><b>Type:</b> xxxxxxxxxxx</p><p><b>Asking Price:</b> $xxxxxxxxx</p><p><b>In:</b> xxxxxxx</p>
        <div class="divider"></div><h3>Want T o House Swap With</h3><p><b>Bed:</b> xx &nbsp;<b>Bath:</b> xx</p><p><b>Type:</b> xxxxxxxxxxxxxxx</p><p><b>In:</b> xxxxxxxxxxxxx</p><p><b>Price Range:</b></p><p>$xxxxxxxxxxxxxxxx</p></article>
      <article class="listing-card"><div class="listing-photo" role="img" aria-label="Photo of a single-storey house with trees"></div>
        <h3>The House I'm Swapping</h3><p><b>Bed:</b> x &nbsp;<b>Bath:</b> x</p><p><b>Type:</b> xxxxxxxxxxx</p><p><b>Asking Price:</b> $xxxxxxxxx</p><p><b>In:</b> xxxxxxx</p>
        <div class="divider"></div><h3>Want T o House Swap With</h3><p><b>Bed:</b> xx &nbsp;<b>Bath:</b> xx</p><p><b>Type:</b> xxxxxxxxxxxxxxx</p><p><b>In:</b> xxxxxxxxxxxxx</p><p><b>Price Range:</b></p><p>$xxxxxxxxxxxxxxxx</p></article>
      <article class="listing-card"><div class="listing-photo" role="img" aria-label="Photo of a single-storey house with trees"></div>
        <h3>The House I'm Swapping</h3><p><b>Bed:</b> x &nbsp;<b>Bath:</b> x</p><p><b>Type:</b> xxxxxxxxxxx</p><p><b>Asking Price:</b> $xxxxxxxxx</p><p><b>In:</b> xxxxxxx</p>
        <div class="divider"></div><h3>Want T o House Swap With</h3><p><b>Bed:</b> xx &nbsp;<b>Bath:</b> xx</p><p><b>Type:</b> xxxxxxxxxxxxxxx</p><p><b>In:</b> xxxxxxxxxxxxx</p><p><b>Price Range:</b></p><p>$xxxxxxxxxxxxxxxx</p></article>
      <article class="listing-card"><div class="listing-photo" role="img" aria-label="Photo of a single-storey house with trees"></div>
        <h3>The House I'm Swapping</h3><p><b>Bed:</b> x &nbsp;<b>Bath:</b> x</p><p><b>Type:</b> xxxxxxxxxxx</p><p><b>Asking Price:</b> $xxxxxxxxx</p><p><b>In:</b> xxxxxxx</p>
        <div class="divider"></div><h3>Want T o House Swap With</h3><p><b>Bed:</b> xx &nbsp;<b>Bath:</b> xx</p><p><b>Type:</b> xxxxxxxxxxxxxxx</p><p><b>In:</b> xxxxxxxxxxxxx</p><p><b>Price Range:</b></p><p>$xxxxxxxxxxxxxxxx</p></article>
    </section>
  </div>
</main>
</body>
</html>
```